tourism marketplace web app redesign*

Hi, I need our front-page redesigned. For the competition please submit a jpg of ABOVE THE FOLD ONLY. The full page redesign will be a revision request. URL is https://qp.vendomix.hu/hu/index.html login:'fullhd' and password:'asdasd' (Fold is supposed to be at "Kiemelt Ajanlatok", use all elements above that. Please use at least one extra color other than the two in the logo, or you may completely change them. FOCUS should be on the central combined search box (3 dropdown, 2 calendar picker + Kereses Button) just like lodgewave.com, staynook.com, Torvil.com, etc... The search box is always large, central, white, we want that too. We want it to look more modern, more clean AND we want to feature a changing beautiful nature photo background (like lodgewave.com).Please use our newly designed logo (in attached pdf) and use that new spelling: "fieldtrek.online"

```html
<!DOCTYPE html>
<html lang="en">
<head>
<meta charset="utf-8">
<title>fieldtrek.online</title>
<link href="https://fonts.googleapis.com/css2?family=Comfortaa:wght@400;600&family=Quicksand:wght@500;600;700&family=Saira+Semi+Condensed:wght@700&display=swap" rel="stylesheet">
<style>
  :root {
    --ink: #333538;
    --ink-soft: #45484c;
    --brand: #5fa88a;
    --brand-btn: #6aaa8e;
    --field: #ffffff;
    --placeholder: #a3a6aa;
    --panel: rgba(70, 75, 80, 0.55);
    --panel-edge: #c9ccd0;
    --white: #ffffff;
  }
  * { box-sizing: border-box; margin: 0; padding: 0; }
  html, body { width: 1200px; height: 675px; overflow: hidden; }
  body { font-family: "Quicksand", sans-serif; color: var(--ink); }
  .hero { position: relative; width: 1200px; height: 675px; overflow: hidden; }
  .hero-photo {
    position: absolute; inset: 0;
    background:
      linear-gradient(180deg, #dfe3ea 0%, #d6dce6 35%, #c3cad6 48%, #9aa2ae 58%, #7d8896 66%, #6e8a6a 74%, #7e8a4e 84%, #6a6a3a 100%);
  }
  .brand { position: absolute; left: 88px; top: 56px; display: flex; align-items: center; gap: 8px; }
  .brand-dot { width: 43px; height: 43px; border-radius: 50%; background: var(--brand); }
  .brand-name { font-family: "Quicksand", sans-serif; font-weight: 700; font-size: 19px; color: var(--ink); letter-spacing: -0.2px; }
  .nav { position: absolute; top: 71px; left: 369px; display: flex; gap: 0; font-size: 11.5px; font-weight: 500; }
  .nav a { position: absolute; white-space: nowrap; color: var(--ink); text-decoration: none; }
  .account { position: absolute; left: 966px; top: 69px; width: 146px; height: 22px; border: 2px solid #5c5f63; display: flex; font-size: 11.5px; font-weight: 500; }
  .account .login { flex: 0 0 104px; display: flex; align-items: center; gap: 18px; padding-left: 12px; border-right: 2px solid #5c5f63; }
  .account .toggle { flex: 1; display: flex; align-items: center; justify-content: center; }
  .prefs { position: absolute; top: 103px; left: 967px; display: flex; font-size: 11.5px; font-weight: 500; }
  .prefs span { display: flex; align-items: center; gap: 12px; }
  .prefs .lang { width: 86px; }
  .headline { position: absolute; top: 204px; left: 0; width: 1200px; text-align: center; font-family: "Saira Semi Condensed", sans-serif; font-weight: 700; font-size: 49px; letter-spacing: 2.4px; color: var(--ink); }
  .tagline { position: absolute; top: 269px; left: 0; width: 1200px; text-align: center; font-family: "Comfortaa", sans-serif; font-size: 30px; color: var(--ink-soft); }
  .search { position: absolute; left: 326px; top: 356px; width: 549px; height: 142px; border: 3px solid var(--panel-edge); background: var(--panel); }
  .tab { position: absolute; top: 11px; color: var(--white); font-weight: 700; font-size: 11.5px; display: flex; align-items: center; gap: 10px; white-space: nowrap; }
  .tab.active::after { content: ""; position: absolute; left: -4px; right: -4px; bottom: -9px; height: 2px; background: var(--white); }
  .field { position: absolute; width: 139px; height: 23px; background: var(--field); border-radius: 2px; font-size: 9.5px; color: var(--placeholder); display: flex; align-items: center; padding-left: 10px; gap: 8px; }
  .search-btn { position: absolute; left: 370px; top: 97px; width: 139px; height: 23px; background: var(--brand-btn); border-radius: 2px; color: var(--white); font-weight: 600; font-size: 10px; display: flex; align-items: center; padding-left: 10px; gap: 30px; }
</style>
</head>
<body>
<main class="hero">
  <div class="hero-photo" role="img" aria-label="Alpine landscape with rocky mountain peaks under a pale sky and green hillsides with a ski lift"></div>

  <div class="brand"><span class="brand-dot"></span><span class="brand-name">fieldtrek.online</span></div>

  <nav class="nav">
    <a style="left:0">Countries</a>
    <a style="left:84px">Wild Species</a>
    <a style="left:183px">About Us</a>
    <a style="left:265px">How it Work</a>
    <a style="left:358px">Term And Condition</a>
  </nav>

  <div class="account">
    <div class="login">
      <svg width="11" height="11" viewBox="0 0 12 12" fill="none" stroke="#45484c" stroke-width="1"><circle cx="6" cy="3.5" r="2.6"/><path d="M1 11.5c0-3 2.2-5 5-5s5 2 5 5"/></svg>
      <span>Login</span>
    </div>
    <div class="toggle"><svg width="12" height="7" viewBox="0 0 12 7" fill="none" stroke="#45484c" stroke-width="1.6"><path d="M1 1l5 5 5-5"/></svg></div>
  </div>

  <div class="prefs">
    <span class="lang">English <svg width="11" height="7" viewBox="0 0 12 7" fill="none" stroke="#45484c" stroke-width="1.6"><path d="M1 1l5 5 5-5"/></svg></span>
    <span>EUR <svg width="11" height="7" viewBox="0 0 12 7" fill="none" stroke="#45484c" stroke-width="1.6"><path d="M1 1l5 5 5-5"/></svg></span>
  </div>

  <h1 class="headline">YOU DON'T NEED HUNTING ORGANIZER!</h1>
  <p class="tagline">Book directly at the hunting ground</p>

  <section class="search">
    <div class="tab active" style="left:61px">Individu Hunt <svg width="11" height="7" viewBox="0 0 12 7" fill="none" stroke="#fff" stroke-width="1.8"><path d="M1 1l5 5 5-5"/></svg></div>
    <div class="tab" style="left:229px">Group Hunt <svg width="11" height="7" viewBox="0 0 12 7" fill="none" stroke="#fff" stroke-width="1.8"><path d="M1 1l5 5 5-5"/></svg></div>
    <div class="tab" style="left:388px">Excluive Packages</div>

    <div class="field" style="left:28px;top:47px">All Wild</div>
    <div class="field" style="left:199px;top:47px">All Country</div>
    <div class="field" style="left:370px;top:47px">All Offers</div>

    <div class="field" style="left:28px;top:97px">
      <svg width="15" height="15" viewBox="0 0 15 15" fill="none" stroke="#b0b3b7" stroke-width="1"><rect x="1" y="2.5" width="13" height="11.5"/><path d="M1 5.5h13M4 1v3M11 1v3"/><path d="M4 8h1M7 8h1M10 8h1M4 11h1M7 11h1M10 11h1" stroke-width="1.5"/></svg>
      dd/mm/yy
    </div>
    <div class="field" style="left:199px;top:97px">
      <svg width="15" height="15" viewBox="0 0 15 15" fill="none" stroke="#b0b3b7" stroke-width="1"><rect x="1" y="2.5" width="13" height="11.5"/><path d="M1 5.5h13M4 1v3M11 1v3"/><path d="M4 8h1M7 8h1M10 8h1M4 11h1M7 11h1M10 11h1" stroke-width="1.5"/></svg>
      dd/mm/yy
    </div>
    <div class="search-btn">
      <svg width="16" height="16" viewBox="0 0 16 16" fill="none" stroke="#fff" stroke-width="1.6"><circle cx="6.5" cy="6.5" r="5.3"/><path d="M10.5 10.5l4.5 4.5"/></svg>
      Search
    </div>
  </section>
</main>
</body>
</html>
```